Business Card Design for Animal Clinic

We are seeking a two sided business card design. The primary side should include our logo (provided in AI and EPS files) address, phone, website, and if possible "Follow Us" with icons for Facebook, Google+, and Twitter.

The back of the card needs to included space for appointment reminders.

Company Name:
Brackenfield Animal Clinic

Doctor Name:
To be provided to winner

Adress:
To be provided to winner

Phone:
to be provided to winner

Website:
www.brackenfieldanimalclinic.example

```html
<!DOCTYPE html>
<html lang="en">
<head>
<meta charset="utf-8">
<title>Brackenfield Animal Clinic – Business Card</title>
<link rel="stylesheet" href="https://fonts.googleapis.com/css2?family=Lora:wght@400;700&family=Lato:wght@400;700&display=swap">
<style>
  :root {
    --clinic-red: #a83a2e;
    --clinic-red-dark: #8f2f25;
    --clinic-rose: #d98c80;
    --ink: #1a1a1a;
    --paper: #ffffff;
    --backdrop: #e9e9e9;
    --rule: #8a8a8a;
  }
  * { box-sizing: border-box; margin: 0; padding: 0; }
  html, body { width: 1200px; height: 926px; overflow: hidden; }
  body {
    background: var(--backdrop);
    font-family: "Lora", Georgia, serif;
    color: var(--ink);
    position: relative;
  }
  .card {
    position: absolute;
    left: 250px;
    width: 700px;
    height: 400px;
    background: var(--paper);
    overflow: hidden;
    box-shadow: 0 2px 10px rgba(0,0,0,0.15);
  }
  .card--front { top: 43px; }
  .card--back { top: 483px; }

  /* Front */
  .front-band {
    position: absolute; left: 0; right: 0; bottom: 0; height: 78px;
    background: var(--clinic-red);
  }
  .clinic-mark {
    position: absolute; left: 38px; top: 34px;
    display: flex; align-items: center; gap: 12px;
  }
  .clinic-mark__dot {
    width: 22px; height: 22px; border-radius: 50%;
    background: var(--clinic-red);
  }
  .clinic-mark__name {
    font-family: "Lora", Georgia, serif;
    font-weight: 400;
    font-size: 24px;
    color: var(--clinic-red);
    letter-spacing: 0.5px;
  }
  .doctor {
    position: absolute; left: 38px; top: 92px;
  }
  .doctor__name {
    font-size: 44px; font-weight: 400; line-height: 1.05;
  }
  .doctor__name strong { font-weight: 700; }
  .doctor__title {
    font-size: 15px; font-weight: 700; color: var(--clinic-red);
    letter-spacing: 1.2px; text-transform: uppercase; margin-top: 2px;
  }
  .contact-list {
    position: absolute; left: 38px; top: 178px;
    list-style: none; font-size: 15.5px; line-height: 24px;
  }
  .contact-list li { display: flex; align-items: flex-start; gap: 10px; }
  .contact-list svg { width: 14px; height: 14px; margin-top: 5px; flex: none; fill: var(--clinic-red); }
  .pet-illustration {
    position: absolute; left: 400px; top: 170px; width: 260px; height: 180px;
    border-radius: 90px 90px 0 0;
    background: linear-gradient(180deg, var(--clinic-red) 0%, var(--clinic-red-dark) 100%);
  }
  .follow {
    position: absolute; right: 30px; bottom: 14px;
    display: flex; align-items: center; gap: 8px;
    color: var(--paper); font-size: 13px; letter-spacing: 1px; text-transform: uppercase;
  }
  .follow__icon {
    width: 18px; height: 18px; border-radius: 50%;
    background: var(--paper); opacity: 0.85;
  }

  /* Back */
  .appointment {
    position: absolute; left: 36px; right: 36px; top: 28px;
    font-family: "Lato", Arial, sans-serif;
  }
  .appointment__title {
    text-align: center; font-size: 24px; font-weight: 700;
    letter-spacing: 3px; text-transform: uppercase; margin-left: 160px;
  }
  .appointment__row {
    display: flex; align-items: flex-end; gap: 12px;
    margin-top: 18px; font-size: 17px;
  }
  .appointment__line { flex: 1; border-bottom: 1.5px solid var(--rule); height: 18px; }
  .back-band {
    position: absolute; left: 0; right: 0; bottom: 0; height: 180px;
    background: var(--clinic-red);
    color: var(--paper);
    font-family: "Lato", Arial, sans-serif;
    font-size: 22px; letter-spacing: 1.5px; line-height: 1.45;
    display: flex; flex-direction: column; align-items: center; justify-content: center;
    text-align: center;
  }
</style>
</head>
<body>

<section class="card card--front" aria-label="Business card front">
  <div class="clinic-mark">
    <span class="clinic-mark__dot"></span>
    <span class="clinic-mark__name">Brackenfield Animal Clinic</span>
  </div>

  <div class="doctor">
    <h1 class="doctor__name">Daniel <strong>Hartley</strong></h1>
    <p class="doctor__title">Veterinary Doctor</p>
  </div>

  <ul class="contact-list">
    <li>
      <svg viewBox="0 0 16 16" aria-hidden="true"><path d="M3 1h3l1.5 4-2 1.2a9 9 0 0 0 4.3 4.3L11 8.5l4 1.5v3a2 2 0 0 1-2 2A13 13 0 0 1 1 3a2 2 0 0 1 2-2z"/></svg>
      <span>123-456-7890</span>
    </li>
    <li>
      <svg viewBox="0 0 16 16" aria-hidden="true"><path d="M1 3h14v10H1z M1 3l7 6 7-6" stroke="#fff" stroke-width="1.2"/></svg>
      <span>yourdomain.com</span>
    </li>
    <li>
      <svg viewBox="0 0 16 16" aria-hidden="true"><path d="M6.5 9.5l3-3M5 8l-2 2a2.5 2.5 0 0 0 3.5 3.5l2-2M11 8l2-2A2.5 2.5 0 0 0 9.5 2.5l-2 2" fill="none" stroke="#a83a2e" stroke-width="1.8" stroke-linecap="round"/></svg>
      <span>yourname@yourdomain.com</span>
    </li>
    <li>
      <svg viewBox="0 0 16 16" aria-hidden="true"><path d="M8 1l7 6.5h-2V15H9.5v-4h-3v4H3V7.5H1z"/></svg>
      <span>Street address goes here, Suite #303,<br>Alt Bldg, NY 82365</span>
    </li>
  </ul>

  <div class="front-band"></div>
  <div class="pet-illustration" role="img" aria-label="Silhouettes of a dog, a rabbit and a cat sitting side by side with small hearts"></div>

  <div class="follow">
    <span>Follow us :</span>
    <span class="follow__icon"></span>
    <span class="follow__icon"></span>
    <span class="follow__icon"></span>
  </div>
</section>

<section class="card card--back" aria-label="Business card back">
  <div class="appointment">
    <h2 class="appointment__title">Appointment</h2>
    <div class="appointment__row"><span>Date:</span><span class="appointment__line"></span></div>
    <div class="appointment__row"><span>Time:</span><span class="appointment__line"></span></div>
    <div class="appointment__row"><span>Location:</span><span class="appointment__line"></span></div>
  </div>
  <div class="back-band">
    <p>Street address goes here, Suite #303,</p>
    <p>Alt Bldg, NY 82365</p>
  </div>
</section>

</body>
</html>
```